Flyer Design für deutsch-türkischen Lebensmittelmarkt
Zielgruppe
deutsch-türkischer Lebensmittelmarkt.
deutsche wie auch türken
Aufgabenstellung
Das Gewinnspiel muss herausstechen

```html
<!DOCTYPE html>
<html lang="de">
<head>
<meta charset="utf-8">
<title>Yildiz Markt – Flyer</title>
<link href="https://fonts.googleapis.com/css2?family=Oswald:wght@600;700&family=Montserrat:wght@400;500;600;700&display=swap" rel="stylesheet">
<style>
:root{
  --green:#6e8430;
  --dark:#333230;
  --beige:#e8c49c;
  --yellow:#f2b705;
  --white:#ffffff;
  --stage:#e4e3e1;
  --brown:#8a6a3c;
}
*{margin:0;padding:0;box-sizing:border-box}
html,body{width:1200px;height:755px;overflow:hidden;background:var(--stage)}
body{position:relative;font-family:"Montserrat",sans-serif;color:var(--dark)}
.page{position:absolute;top:89px;width:407px;height:576px;background:var(--white);overflow:hidden}
.page--front{left:175px}
.page--offers{left:618px}
.page-bg{position:absolute;inset:0}
.headline{font-family:"Oswald",sans-serif;font-weight:700;text-transform:uppercase;position:absolute;right:23px;text-align:right;line-height:1.08;white-space:nowrap}
.front-title{top:18px;font-size:26px;color:var(--white)}
.front-sub{top:82px;font-size:12px;color:var(--beige);font-weight:600}
.photo{position:absolute}
.logo{position:absolute;background:var(--white);border-radius:50%;border-bottom:3px solid #ccc;display:flex;flex-direction:column;align-items:center;justify-content:center;gap:4px}
.logo-row{display:flex;align-items:center;gap:5px}
.logo-dot{width:12px;height:12px;border-radius:50%;background:var(--green)}
.logo-name{font-weight:700;font-size:12px;color:var(--brown)}
.logo-tag{font-size:4.5px;font-weight:600;color:var(--dark)}
.checklist{position:absolute;top:315px;left:23px;list-style:none;font-size:8.6px;font-weight:500;line-height:12px}
.checklist li{display:flex;align-items:center;gap:8px}
.checklist svg{width:10px;height:8px}
.contest-title{position:absolute;top:410px;left:23px;font-family:"Oswald",sans-serif;font-weight:700;font-size:26px;color:var(--dark)}
.contest-lead{position:absolute;top:450px;left:23px;font-size:10.6px;font-weight:700;color:var(--dark);line-height:15px;white-space:nowrap}
.contest-tr{position:absolute;top:481px;left:23px;font-size:8.4px;white-space:nowrap}
.contest-rule{position:absolute;top:507px;left:23px;font-size:8.2px;font-weight:700;line-height:12px;white-space:nowrap}
.contest-fine{position:absolute;top:508px;left:168px;font-size:5.3px;line-height:9.2px;white-space:nowrap}
.address{position:absolute;top:24px;left:23px;font-size:5.3px;line-height:9.2px;color:var(--dark);font-style:normal}
.address b{font-weight:700}
.offer-date{top:20px;font-size:16px;color:var(--white);text-transform:none}
.offer-title{top:42px;font-size:25px;color:var(--white)}
.offer-sub{top:76px;font-size:11.5px;color:var(--beige);font-weight:600}
.grid{position:absolute;top:187px;left:23px;display:grid;grid-template-columns:repeat(3,112px);grid-auto-rows:112px;column-gap:12px;row-gap:14px}
.item{position:relative;border:1px solid #cfcfcf;background:var(--white)}
.item-photo{height:86px}
.item-name{position:absolute;left:0;right:0;bottom:0;height:26px;background:var(--dark);color:var(--white);font-size:7.6px;font-weight:500;display:flex;align-items:center;padding-left:7px;line-height:9px}
.price{position:absolute;top:-10px;right:-8px;width:42px;height:42px;border-radius:50%;background:var(--green);color:var(--white);display:flex;flex-direction:column;align-items:center;justify-content:center;font-weight:700;font-size:9px;line-height:10px;box-shadow:0 1px 2px rgba(0,0,0,.25)}
.price small{font-size:5px;font-weight:500}
.price--hot{background:var(--yellow);color:var(--dark)}
.tag-hot{position:absolute;top:-12px;right:-27px;background:var(--yellow);font-size:5.5px;padding:1px 4px;color:var(--dark)}
.tag-hot::before{content:"";position:absolute;left:-9px;top:-5px;width:11px;height:11px;background:var(--yellow);clip-path:polygon(50% 0,61% 35%,98% 35%,68% 57%,79% 91%,50% 70%,21% 91%,32% 57%,2% 35%,39% 35%)}
.tag-butcher{position:absolute;top:7px;left:10px;background:var(--beige);font-size:5.2px;line-height:6px;padding:1px 5px;text-align:center;color:var(--dark)}
</style>
</head>
<body>

<section class="page page--front">
  <svg class="page-bg" viewBox="0 0 407 576" aria-hidden="true">
    <path d="M0 0H407V130C370 190 310 180 250 140C190 100 120 95 0 120Z" fill="var(--green)"/>
    <path d="M0 105C80 80 170 90 230 130C290 172 360 205 407 165V200C350 215 290 190 240 160C170 118 90 100 0 120Z" fill="var(--beige)"/>
    <path d="M0 255C90 285 200 300 300 305C350 308 390 300 407 292V307C380 318 330 322 290 320C190 315 90 295 0 275Z" fill="var(--dark)"/>
    <path d="M0 373C80 390 150 388 245 373V576H0Z" fill="var(--beige)"/>
    <path d="M245 373C310 360 370 320 407 300V576H245Z" fill="var(--beige)"/>
  </svg>
  <h1 class="headline front-title">Weil Sie bei uns im<br>Mittelpunkt stehen</h1>
  <p class="headline front-sub">Günkü bizde ortada durdugunuz icin</p>

  <div class="photo" role="img" aria-label="Schale mit grünen und schwarzen Oliven" style="left:0;top:116px;width:148px;height:112px;border-radius:0 60px 60px 0;background:radial-gradient(circle at 45% 55%,#6d7a2a,#b7a25c 60%,#e9dcc0)"></div>
  <div class="photo" role="img" aria-label="Schmortopf mit Gulasch" style="left:150px;top:130px;width:128px;height:160px;border-radius:0 0 40px 60px;background:radial-gradient(circle at 55% 50%,#9a3a1c,#4a2a1a 60%,#2a1f18)"></div>
  <div class="photo" role="img" aria-label="Fleischspieße vom Grill" style="left:278px;top:205px;width:129px;height:93px;border-radius:30px 0 0 40px;background:linear-gradient(135deg,#7a5a48,#a06a55 50%,#4a3a30)"></div>

  <div class="logo" style="left:18px;top:212px;width:112px;height:86px">
    <div class="logo-row"><span class="logo-dot"></span><span class="logo-name">Yildiz Markt</span></div>
    <span class="logo-tag">deutsch-türkischer Lebensmittelmarkt</span>
  </div>

  <ul class="checklist">
    <li><svg viewBox="0 0 10 8"><path d="M1 4l3 3 5-6" stroke="var(--green)" stroke-width="1.6" fill="none"/></svg>Obst &amp; Gemüse vom Großmarkt, München</li>
    <li><svg viewBox="0 0 10 8"><path d="M1 4l3 3 5-6" stroke="var(--green)" stroke-width="1.6" fill="none"/></svg>Fleisch von der Firma Karaberg, Mengen</li>
    <li><svg viewBox="0 0 10 8"><path d="M1 4l3 3 5-6" stroke="var(--green)" stroke-width="1.6" fill="none"/></svg>Große Auswahl an frischen Backprodukten</li>
    <li><svg viewBox="0 0 10 8"><path d="M1 4l3 3 5-6" stroke="var(--green)" stroke-width="1.6" fill="none"/></svg>Eingelegte Oliven, Paprika und vieles mehr</li>
  </ul>

  <div class="photo" role="img" aria-label="Goldmünzen auf rotem Band" style="left:228px;top:370px;width:179px;height:104px;border-radius:60px 0 0 60px;background:radial-gradient(circle at 40% 60%,#c9a24a,#e6cf8a 35%,#b02a40 70%,#fff)"></div>

  <h2 class="contest-title">GEWINNSPIEL</h2>
  <p class="contest-lead">Gewinnen Sie bei Yildiz Markt eine<br>Goldmünze im Wert von ca. 65€.</p>
  <p class="contest-tr">Yildiz Markt’ta 65€ degerinde bir ceyrek altin kazanin</p>
  <p class="contest-rule">Ab einem Einkaufswert von<br>30€ nehmen Sie an unserem<br>Gewinnspiel teil. Wir verlosen<br>insgesamt 12 Münzen.</p>
  <p class="contest-fine">Nach Ihrem Einkauf kommt Ihr Kassenzettel mit Ihren Daten (Name, Telnr.)<br>in eine verschlossene Losbox und wird live auf Kanalo an den 4 darauf<br>folgenden Samstaggabenden (16.09./23.09/30.09/07.10.17) um 20 Uhr<br>gezogen, wir verlosen 3 Stück jede Woche. Nutzen Sie Ihre Chance einer<br>von 10 glücklichen Gewinnern zu sein.</p>
</section>

<section class="page page--offers">
  <svg class="page-bg" viewBox="0 0 407 576" aria-hidden="true">
    <path d="M0 0H407V125C370 175 310 160 250 130C180 100 90 90 0 110Z" fill="var(--green)"/>
    <path d="M0 100C80 95 170 100 230 120C280 138 310 150 290 152C200 130 100 120 0 160Z" fill="var(--beige)"/>
    <path d="M250 148C310 170 370 175 407 128V150C380 175 330 178 270 158Z" fill="var(--dark)"/>
  </svg>
  <address class="address"><b>Yildiz Markt</b><br>Musterstraße 1<br>12345 Musterstadt<br>+49 (0)1234 5678910<br>info@yildizmarkt.de</address>
  <p class="headline offer-date">11.9. bis 7.10.2017</p>
  <h1 class="headline offer-title">Aktuelle Angebote</h1>
  <p class="headline offer-sub">Ürünindirmlerimiz kampanyalarimiz</p>

  <div class="logo" style="left:16px;top:78px;width:124px;height:86px">
    <div class="logo-row"><span class="logo-dot"></span><span class="logo-name">Yildiz Markt</span></div>
    <span class="logo-tag">deutsch-türkischer Lebensmittelmarkt</span>
  </div>

  <div class="grid">
    <article class="item"><div class="item-photo" role="img" aria-label="Sesamringe Simit" style="background:linear-gradient(135deg,#b76a2a,#e0a25a)"></div><span class="tag-hot">Highlight</span><div class="price price--hot">0,69€<small>/Stk</small></div><p class="item-name">Simit</p></article>
    <article class="item"><div class="item-photo" role="img" aria-label="Stücke Su Böregi auf Teller" style="background:linear-gradient(135deg,#e8e2d6,#e6c878)"></div><span class="tag-hot">Highlight</span><div class="price price--hot">0,99€<small>/Stk</small></div><p class="item-name">Su Böregi</p></article>
    <article class="item"><div class="item-photo" role="img" aria-label="Rohe Lammkeule mit Rosmarin" style="background:linear-gradient(135deg,#f0ece6,#e2a8a8)"></div><span class="tag-butcher">aus unserer<br>Metzgerei</span><div class="price">11,49€<small>/kg</small></div><p class="item-name">Lammkeule</p></article>

    <article class="item"><div class="item-photo" role="img" aria-label="Rinderhackfleisch mit Zwiebeln" style="background:linear-gradient(135deg,#c9b26a,#c4605a)"></div><span class="tag-butcher">aus unserer<br>Metzgerei</span><div class="price">5,99€<small>/kg</small></div><p class="item-name">Rinderhackleisch</p></article>
    <article class="item"><div class="item-photo" role="img" aria-label="Reispackung" style="background:radial-gradient(circle,#e88a8a,#fff 70%)"></div><div class="price">4,99€<small>/5kg</small></div><p class="item-name">Beyazgül Reis</p></article>
    <article class="item"><div class="item-photo" role="img" aria-label="Teepackungen" style="background:radial-gradient(circle,#4a4a48,#fff 75%)"></div><div class="price">4,99€<small>/1kg</small></div><p class="item-name">Selvi yaprak cay</p></article>

    <article class="item"><div class="item-photo" role="img" aria-label="Packung rote Linsen" style="background:radial-gradient(circle,#d0442a,#fff 65%)"></div><div class="price">1,89€<small>/1kg</small></div><p class="item-name">Anadol rote Linsen</p></article>
    <article class="item"><div class="item-photo" role="img" aria-label="Packung Sonnenblumenkerne" style="background:radial-gradient(circle,#e08a2a,#fff 65%)"></div><div class="price">0,89€<small>/500g</small></div><p class="item-name">Doruk<br>Sonnenblumenkerne</p></article>
    <article class="item"><div class="item-photo" role="img" aria-label="Fleischspieße vom Grill" style="background:linear-gradient(135deg,#5a4638,#9a6a52)"></div><div class="price">11,49€<small>/kg</small></div><p class="item-name">Lorem ipsum</p></article>
  </div>
</section>

</body>
</html>
```